Website Redesign Project Puzzle Vault Leesburg

We are an escape room company located in Ashburn, Virginia. We currently have a website https://www.puzzlevaultleesburg.example based upon html/bootstrap/javascript/php/mysql and I'd like to keep it that way. I'm looking for someone upgrade the front page so it is more informative, cleaner, quicker to load, and optimizes the space for full sale opportunities.

Target Market(s)

Corporate Clients, Families, Friends. All ages

Industry/Entity Type

Entertainment Industry

Coding

Font styles to use
Other font styles liked:
• Similar to Facebook or Amazon

Requirements
Must have
• Must be mobile friendly. bootstrap. Lots of graphics (will provide) nice and easy to read fonts. Easy to read layout. Must look clean, fresh, exciting, and want to grab attention.
• Please visit my facebook page and website for more details. facebook.com/puzzlevaultleesburg
Nice to have
• Same color as existing but open to options if they look nice.
Should not have
• Should not be wordpress or hard to modify.

```html
<!DOCTYPE html>
<html lang="en">
<head>
<meta charset="utf-8">
<title>Puzzle Vault Leesburg</title>
<link rel="stylesheet" href="https://fonts.googleapis.com/css2?family=Mulish:wght@400;600;700;800&display=swap">
<style>
:root{
  --navy:#1c2a6e;
  --navy-dark:#142057;
  --blue:#0ea5e9;
  --ink:#1e2440;
  --muted:#6b7086;
  --line:#e3e5ec;
  --soft:#f4f5f8;
  --white:#ffffff;
}
*{box-sizing:border-box;margin:0;padding:0}
html,body{width:1200px;height:4826px;overflow:hidden}
body{font-family:"Mulish",Arial,sans-serif;color:var(--ink);background:var(--white);font-size:14px;line-height:1.55}
section,header,footer{position:relative;width:1200px}
.btn{display:inline-block;border-radius:20px;font-size:12px;font-weight:800;letter-spacing:.5px;text-transform:uppercase;padding:9px 26px;color:var(--white);background:var(--navy)}
.btn-blue{background:var(--blue)}
.btn-white{background:var(--white);color:var(--navy)}
.section-title{text-align:center;font-size:36px;font-weight:800;color:var(--navy)}
.section-title span{color:var(--blue)}

/* hero */
.hero{height:715px;overflow:hidden}
.hero-photo{position:absolute;inset:0;background:radial-gradient(ellipse at 50% 45%,#6b3a2a 0%,#3a2620 45%,#15141a 100%)}
.hero-shade{position:absolute;inset:0;background:rgba(10,12,20,.45)}
.topbar{position:absolute;left:90px;right:90px;top:28px;display:flex;align-items:center}
.brand{display:flex;align-items:center;gap:12px;color:var(--blue);font-weight:800;font-size:22px;line-height:1.1;width:300px}
.brand-mark{width:34px;height:34px;background:var(--blue);border-radius:4px}
.contact-top{display:flex;gap:40px;margin-left:180px;color:var(--white);font-size:12px}
.contact-top div{display:flex;gap:10px;align-items:center}
.contact-top small{display:block;font-size:10px;font-weight:700;opacity:.8}
.contact-top svg{width:26px;height:26px}
.topbar .btn{margin-left:auto}
.nav{position:absolute;right:90px;top:110px;display:flex;gap:34px;font-size:14px;font-weight:700;color:var(--white)}
.nav .active{color:var(--blue)}
.hero-copy{position:absolute;top:390px;width:100%;text-align:center;color:var(--white)}
.hero-copy h1{font-size:38px;font-weight:800;line-height:1.25}
.hero-copy .btn{margin-top:26px}
.dots{position:absolute;top:662px;width:100%;display:flex;justify-content:center;gap:10px}
.dots i{width:12px;height:12px;border-radius:50%;border:2px solid rgba(255,255,255,.7)}
.dots i:first-child{background:var(--white)}

/* rooms */
.rooms{height:749px;padding-top:74px}
.room-grid{position:absolute;top:179px;left:90px;display:flex;gap:29px}
.room{width:235px;height:490px;padding:0 0 0 0;position:relative}
.room.featured{box-shadow:0 10px 30px rgba(20,30,80,.15);background:var(--white)}
.room-photo{height:200px}
.room-body{padding:22px 8px 0}
.room.featured .room-body{padding:22px 18px 0}
.room h3{font-size:18px;font-weight:800;color:var(--navy)}
.room .diff{font-size:13px;font-weight:700;color:var(--blue);margin-bottom:8px}
.room p{font-size:13px;color:var(--muted);line-height:1.5}
.room .btn{position:absolute;bottom:20px;left:8px}
.room.featured .btn{left:18px}

/* corporate */
.corporate{height:476px}
.corporate-photo{position:absolute;inset:0;background:linear-gradient(180deg,#4f5f7a 0%,#7a6a62 55%,#5a4a48 100%)}
.corporate-photo::after{content:"";position:absolute;inset:0;background:rgba(20,20,35,.25)}
.corporate h2{position:absolute;top:205px;width:100%;text-align:center;font-size:38px;font-weight:800;color:var(--white);z-index:1}

/* packages */
.packages{height:590px;padding-top:74px}
.package-grid{position:absolute;top:173px;left:90px;display:flex;gap:20px}
.package{width:325px;height:300px;background:var(--soft)}
.package-head{height:91px;background:var(--navy);color:var(--white);font-weight:800;font-size:15px;padding:24px 22px;line-height:1.35}
.package.mid .package-head{background:var(--blue)}
.package p{padding:22px 22px 0;font-size:13px;color:var(--muted);height:160px}
.package .players{padding:0 22px;font-size:13px;font-weight:700;color:var(--blue)}
.packages .btn{position:absolute;top:524px;left:50%;transform:translateX(-50%)}

/* birthday */
.birthday{height:580px}
.bday-photo{position:absolute;left:90px;top:43px;width:495px;height:493px;background:linear-gradient(160deg,#1c2b5c 0%,#3b2a6e 50%,#a12a3c 100%);box-shadow:0 10px 30px rgba(0,0,0,.2)}
.bday-copy{position:absolute;left:643px;top:80px;width:467px}
.bday-copy h2{font-size:36px;font-weight:800;color:var(--navy);margin-bottom:22px}
.bday-copy h2 span{color:var(--blue)}
.bday-copy p{font-size:13px;color:var(--muted);margin-bottom:12px}
.bday-copy b{color:var(--blue)}
.bday-copy .btn{margin-top:22px}

/* message */
.message{height:445px;padding-top:36px}
.form{position:absolute;left:225px;top:113px;width:755px;display:grid;grid-template-columns:repeat(3,1fr);gap:16px}
.field{height:36px;border:1px solid var(--line);font-size:12px;color:#a3a7b6;padding:9px 14px}
.field.wide{grid-column:span 2;display:flex;justify-content:space-between}
.field.span3{grid-column:span 3;height:100px}
.message .btn{position:absolute;top:335px;left:50%;transform:translateX(-50%)}

/* band */
.band{height:283px;background:var(--blue);color:var(--white);text-align:center;padding-top:68px}
.band p{width:760px;margin:0 auto;font-size:16px;font-weight:600;line-height:1.6}
.band .btn{margin-top:38px}

/* how it works */
.how{height:608px;padding-top:70px}
.faq{position:absolute;left:90px;top:170px;width:1020px}
.faq-item{border-bottom:1px solid var(--line);padding:14px 14px;display:flex;justify-content:space-between;align-items:flex-start;font-size:14px;font-weight:700;color:var(--navy)}
.faq-item .answer{font-weight:400;font-size:13px;color:var(--muted);margin-top:8px;width:900px}
.faq-item svg{width:18px;height:18px;flex:none}
.how .btn{position:absolute;top:495px;left:50%;transform:translateX(-50%)}

/* footer */
.footer{height:380px;background:var(--navy);color:var(--white)}
.foot-brand{position:absolute;left:90px;top:64px;display:flex;gap:12px;align-items:center;color:var(--blue);font-size:22px;font-weight:800;width:230px;line-height:1.15}
.foot-col{position:absolute;top:60px;font-size:13px}
.foot-col h4{color:var(--blue);font-size:16px;font-weight:800;margin-bottom:12px}
.foot-col li{list-style:none;line-height:1.9}
.foot-col .hi{color:var(--blue)}
.foot-col b{color:var(--blue)}
.copy{position:absolute;left:0;right:0;bottom:0;height:64px;border-top:1px solid rgba(255,255,255,.15);display:flex;align-items:center;padding:0 90px;font-size:12px}
.social{margin-left:auto;display:flex;gap:12px}
.social i{width:28px;height:28px;border-radius:50%;background:rgba(255,255,255,.25)}
.social i:nth-child(2){background:var(--blue)}
</style>
</head>
<body>

<header class="hero">
  <div class="hero-photo" role="img" aria-label="Group of players in orange jumpsuits smiling inside an escape room"></div>
  <div class="hero-shade"></div>
  <div class="topbar">
    <div class="brand"><span class="brand-mark"></span>Puzzle Vault Leesburg</div>
    <div class="contact-top">
      <div>
        <svg viewBox="0 0 24 24"><circle cx="12" cy="12" r="11" fill="#0ea5e9"/><path d="M8 7l2 0 1 3-1.5 1a6 6 0 003 3l1-1.5 3 1 0 2a1 1 0 01-1 1A9 9 0 017 8a1 1 0 011-1z" fill="#fff"/></svg>
        <span><small>CALL US</small>(571) 555-0142</span>
      </div>
      <div>
        <svg viewBox="0 0 24 24"><circle cx="12" cy="12" r="11" fill="#0ea5e9"/><rect x="6" y="8" width="12" height="8" fill="none" stroke="#fff" stroke-width="1.5"/><path d="M6 8l6 5 6-5" fill="none" stroke="#fff" stroke-width="1.5"/></svg>
        <span><small>EMAIL US</small>hello@puzzlevaultleesburg.example</span>
      </div>
    </div>
    <span class="btn btn-blue">Book Now</span>
  </div>
  <nav class="nav">
    <span class="active">Home</span><span>Escape Room</span><span>Special Events</span><span>Locations</span><span>How It Works</span><span>Contact Us</span>
  </nav>
  <div class="hero-copy">
    <h1>Our Quest Rooms will<br>give you all spectrum of emotions</h1>
    <span class="btn btn-blue">Contact Us</span>
  </div>
  <div class="dots"><i></i><i></i><i></i></div>
</header>

<section class="rooms">
  <h2 class="section-title"><span>Escape</span> Rooms</h2>
  <div class="room-grid">
    <article class="room">
      <div class="room-photo" role="img" aria-label="Elevator room with folding metal gate" style="background:linear-gradient(135deg,#d9dde4,#8c96a6)"></div>
      <div class="room-body">
        <h3>Elevator</h3><div class="diff">Difficulty: 10/10</div>
        <p>The main elevators are down so you'll need to take the freight elevator to the top floor. If you want to get your second, the last celebrity that attempted to do so wasn't so lucky.</p>
      </div>
      <span class="btn">Book Now!</span>
    </article>
    <article class="room featured">
      <div class="room-photo" role="img" aria-label="Colourful candy shop room with striped decor" style="background:linear-gradient(135deg,#e24a4a,#f4c2a8 60%,#7fb6d9)"></div>
      <div class="room-body">
        <h3>Candy Shop</h3><div class="diff">Difficulty: 7/10</div>
        <p>With all of the candy right before your eyes, find the golden ticket and win the prize!</p>
      </div>
      <span class="btn btn-blue">Book Now!</span>
    </article>
    <article class="room">
      <div class="room-photo" role="img" aria-label="Bank vault room with safe door" style="background:linear-gradient(135deg,#4b4f57,#9a9ea6)"></div>
      <div class="room-body">
        <h3>Bank Heist</h3><div class="diff">Difficulty: 8/10</div>
        <p>With your family held hostage, the mob gave you one choice - rob the bank in exchange for their freedom or kiss its goodbyes forever.</p>
      </div>
      <span class="btn">Book Now!</span>
    </article>
    <article class="room">
      <div class="room-photo" role="img" aria-label="Players in orange prison jumpsuits in a jail cell" style="background:linear-gradient(135deg,#6a4a3a,#d26a2a)"></div>
      <div class="room-body">
        <h3>Jail Break</h3><div class="diff">Difficulty: 8/10</div>
        <p>One Guard, One Goal: get out.</p>
      </div>
      <span class="btn">Book Now!</span>
    </article>
  </div>
</section>

<section class="corporate">
  <div class="corporate-photo" role="img" aria-label="Large corporate team posing together in the lobby"></div>
  <h2>Corporate Events</h2>
</section>

<section class="packages">
  <h2 class="section-title"><span>Our</span> Packages</h2>
  <div class="package-grid">
    <article class="package">
      <div class="package-head">On-Site Multi-Room Packages</div>
      <p>Come, enjoy, relax in our multi room escape room facility with your team. With four different rooms to choose from we are able to accommodate up to 30 people in a single hour.</p>
      <div class="players">Number of Players: 30+</div>
    </article>
    <article class="package mid">
      <div class="package-head">Off-Site Hot Seat Escape Room Package</div>
      <p>Enjoy a 2 or 4 hour escape room in the new thrilling Hot Seat challenge! Each player is given ten minutes to solve the challenge at hand before they go up in smoke! Can you do it?</p>
      <div class="players">Number of Players: 20 to 100</div>
    </article>
    <article class="package">
      <div class="package-head">Off-Site Customer Escape Room to Fit any Space you Provide Us</div>
      <p>Enjoy a customized escape room game to fit the theme you'd like to celebrate. You and your team will come in to work or what seems to be a normal work day until they enter an immersive experience for all to enjoy. Each game is customized and includes live actors.</p>
      <div class="players">Number of Players: 30+</div>
    </article>
  </div>
  <span class="btn">Book Your Package!</span>
</section>

<section class="birthday">
  <div class="bday-photo" role="img" aria-label="Family celebrating a birthday inside the elevator room under red lights"></div>
  <div class="bday-copy">
    <h2><span>Birthday</span> Parties</h2>
    <p>Celebrate this year in style by treating your family with an escape room birthday package. You and your loved ones have the choice of two escape rooms and will enjoy a private party afterwards in our party room. Either of these packages will be sure to satisfy your needs.</p>
    <p><b>A.</b> A private escape room event with party room pizza and soda. Add just <b>$150</b> to your escape room.</p>
    <p><b>B.</b> A private escape room event with a party room rental. Bring your own food. Add just <b>$125</b></p>
    <p><b>Note:</b> A <b>$50</b> cleaning fee applies to all parties who don't clean after themselves.</p>
    <span class="btn">Book Now!</span>
  </div>
</section>

<section class="message">
  <h2 class="section-title"><span>Send Us</span> Message</h2>
  <div class="form">
    <div class="field">Name</div>
    <div class="field">Email</div>
    <div class="field">Phone</div>
    <div class="field">Group Size</div>
    <div class="field wide"><span>Which Package</span><span>&#9662;</span></div>
    <div class="field span3">Message</div>
  </div>
  <span class="btn">Send</span>
</section>

<section class="band">
  <p>An escape room is a themed environment where you and your friends must work together to complete the objectives through solving puzzles before time runs out. Most missions will lock you in while some of our missions do not.</p>
  <span class="btn btn-white">Book Your Room!</span>
</section>

<section class="how">
  <h2 class="section-title"><span>How it</span> Works</h2>
  <div class="faq">
    <div class="faq-item"><span>How do I make a reservation?</span><svg viewBox="0 0 18 18"><circle cx="9" cy="9" r="8" fill="none" stroke="#1c2a6e"/><path d="M9 5v8M5 9h8" stroke="#1c2a6e"/></svg></div>
    <div class="faq-item"><div>Is there an age limit<div class="answer">Participants 12 and older can be by themselves as long as an adult signs the waivers and is available for emergencies. Participants under 12 must be accompanied by an adult in the room or at the facility.</div></div><svg viewBox="0 0 18 18"><circle cx="9" cy="9" r="8" fill="#0ea5e9"/><path d="M5 9h8" stroke="#fff"/></svg></div>
    <div class="faq-item"><span>I'm pregnant, can I participate?</span><svg viewBox="0 0 18 18"><circle cx="9" cy="9" r="8" fill="none" stroke="#1c2a6e"/><path d="M9 5v8M5 9h8" stroke="#1c2a6e"/></svg></div>
    <div class="faq-item"><span>How can I redeem a voucher or promo code?</span><svg viewBox="0 0 18 18"><circle cx="9" cy="9" r="8" fill="none" stroke="#1c2a6e"/><path d="M9 5v8M5 9h8" stroke="#1c2a6e"/></svg></div>
    <div class="faq-item"><span>Where do I park?</span><svg viewBox="0 0 18 18"><circle cx="9" cy="9" r="8" fill="none" stroke="#1c2a6e"/><path d="M9 5v8M5 9h8" stroke="#1c2a6e"/></svg></div>
  </div>
  <span class="btn btn-blue">Load More</span>
</section>

<footer class="footer">
  <div class="foot-brand"><span class="brand-mark"></span>Puzzle Vault Leesburg</div>
  <div class="foot-col" style="left:376px">
    <h4>Quick Links</h4>
    <ul><li>Home</li><li class="hi">Escape Room</li><li>Special Events</li><li>Locations</li><li>How It Works</li><li>Contact Us</li></ul>
  </div>
  <div class="foot-col" style="left:579px">
    <h4>Contact Us</h4>
    <ul><li><b>Call Us:</b> (571) 555-0142</li><li><b>Email:</b> hello@puzzlevaultleesburg.example</li><li><b>Address</b></li><li>18 Example Plaza, Suite 210,<br>Leesburg, VA 20175</li></ul>
  </div>
  <div class="foot-col" style="left:845px">
    <h4>Working Hours</h4>
    <ul><li>Wednesday - Friday (4 to 10pm)</li><li>Saturday - Sunday (11am to 11pm)</li></ul>
  </div>
  <div class="copy">
    <span>© 2019 Puzzle Vault Leesburg. All Right Reserved</span>
    <div class="social"><i></i><i></i><i></i></div>
  </div>
</footer>

</body>
</html>
```